Property investment company needs a letterhead design!

We are a new residential and commercial property investment company. Name of the company is Morvesta Group, LLC. We have a new logo and now we need letterhead! We prefer to have a professional and upscale appearance. We don't have any fixed requirements, so be creative! Thank you for considering this project. We are so excited to see what happens!

Target Market(s)

Professional

Industry/Entity Type

Real Estate Development

```html
<!DOCTYPE html>
<html lang="en">
<head>
<meta charset="utf-8">
<title>Morvesta Group, LLC — Letterhead</title>
<link rel="stylesheet" href="https://fonts.googleapis.com/css2?family=Montserrat:wght@300;400;500;700&family=Arimo:wght@400&display=swap">
<style>
  :root {
    --navy: #03213f;
    --sky: #0aa3e3;
    --ink: #3a3a3a;
    --muted: #8c8c8c;
    --paper: #ffffff;
    --backdrop: #eef1f5;
  }
  * { box-sizing: border-box; margin: 0; padding: 0; }
  html, body { width: 1200px; height: 1200px; overflow: hidden; background: var(--backdrop); }
  .letterhead {
    position: absolute; left: 190px; top: 20px;
    width: 821px; height: 1160px;
    background: var(--paper);
    font-family: "Montserrat", sans-serif;
    color: var(--muted);
    overflow: hidden;
  }
  .header-band { position: absolute; left: 0; top: 0; width: 100%; height: 59px; background: var(--navy); }
  .header-rule { position: absolute; left: 0; top: 59px; width: 100%; height: 5px; background: var(--sky); }
  .brand-disc {
    position: absolute; left: 50px; top: 16px; width: 134px; height: 134px;
    border-radius: 50%; background: var(--paper);
  }
  .brand-name {
    position: absolute; left: 40px; top: 86px; width: 154px;
    text-align: center; font-weight: 700; font-size: 22px; line-height: 24px;
    color: var(--navy); letter-spacing: 0.5px;
  }
  .brand-name span { display: block; font-size: 11px; line-height: 16px; letter-spacing: 3px; }
  .company-address {
    position: absolute; left: 629px; top: 19px;
    font-family: "Arimo", sans-serif; font-size: 13px; line-height: 16px; color: var(--paper);
  }
  .contact-list { position: absolute; left: 629px; top: 75px; list-style: none; }
  .contact-list li {
    display: flex; align-items: center; gap: 7px;
    font-family: "Arimo", sans-serif; font-size: 13px; line-height: 18px; color: var(--ink);
  }
  .contact-list svg { width: 10px; height: 10px; flex: none; }
  .contact-list .accent { color: var(--sky); }
  .recipient { position: absolute; left: 85px; top: 258px; }
  .recipient-label { font-size: 14px; font-weight: 500; letter-spacing: 3px; color: var(--ink); }
  .recipient-name { margin-top: 7px; font-size: 14px; font-weight: 500; color: var(--sky); }
  .recipient-address { margin-top: 5px; font-size: 11px; font-weight: 300; line-height: 18px; }
  .letter-date { position: absolute; right: 82px; top: 259px; font-size: 11.5px; font-weight: 400; color: var(--muted); }
  .letter-body { position: absolute; left: 85px; top: 409px; width: 655px; }
  .letter-body p {
    font-size: 11.6px; font-weight: 300; line-height: 14.5px;
    text-align: justify; margin-bottom: 14.5px; color: var(--muted);
  }
  .signature-mark {
    position: absolute; left: 85px; top: 822px; width: 140px; height: 32px;
    background: linear-gradient(90deg, #f1f2f4, #e7e9ec); border-radius: 3px;
  }
  .signatory { position: absolute; left: 82px; top: 862px; }
  .signatory-name { font-size: 13px; font-weight: 500; color: var(--ink); letter-spacing: 0.5px; }
  .signatory-title { margin-top: 2px; font-size: 10.5px; font-weight: 300; }
</style>
</head>
<body>
  <main class="letterhead">
    <div class="header-band"></div>
    <div class="header-rule"></div>
    <div class="brand-disc"></div>
    <div class="brand-name">MORVESTA<span>GROUP, LLC</span></div>

    <address class="company-address">2240-B Harrow Lane, city<br>state, ZIP 0000</address>
    <ul class="contact-list">
      <li><svg viewBox="0 0 10 10"><path fill="#0aa3e3" d="M2 0.5l2 2-1 1.2c.6 1.3 1.6 2.3 2.9 2.9L7 5.6l2 2-1.3 1.8C4.3 9.3.7 5.7.6 2.3z"/></svg>555-318-2100</li>
      <li><svg viewBox="0 0 10 10"><rect x="0.5" y="2" width="9" height="6.5" fill="#0aa3e3"/><path d="M0.8 2.3 5 5.6 9.2 2.3" stroke="#fff" stroke-width="0.9" fill="none"/></svg>hello@morvestagroup.com</li>
      <li><svg viewBox="0 0 10 10"><circle cx="5" cy="5" r="4.5" fill="#0aa3e3"/><path d="M0.5 5h9M5 .5c-2.2 2.6-2.2 6.4 0 9M5 .5c2.2 2.6 2.2 6.4 0 9" stroke="#fff" stroke-width="0.7" fill="none"/></svg><span>www.<span class="accent">morvestagroup</span>.com</span></li>
    </ul>

    <section class="recipient">
      <div class="recipient-label">TO</div>
      <div class="recipient-name">Dana Kellerby</div>
      <div class="recipient-address">Human Resources<br>Larkspur Holdings Inc.<br>2240-B Harrow Lane, Eastfield<br>E41 USA</div>
    </section>
    <time class="letter-date" datetime="2018-01-01">Friday, 01/01/2018</time>

    <article class="letter-body">
      <p>Lorem ipsum dolor sit amet, consectetuer adipiscing elit, sed diam nonmmy nibh euismod tincidunt ut laoreet dolore magna aliquam erat volutpat. Ut wisi enim ad minim veniam, quis nostrud exerci tationmcorper suscipit lobortis nisl ut aliquip ex ea commodo consequat. Duis autem vel eum iriure dolor in hendrerit in vulputate velit esse molestie consequat, vel illum dolore eu feugiat nulla facilisis at vero eros et accumsan et iusto odio dignissim qui blandit praesent luptatum zzril delenit augue duis dolore te feugait nulla facilisi.</p>
      <p>Nam liber tempor cum soluta nobis eleifend option congue nihil imprdiet doming id quod mazim placerat facer possim assum. Typi non habent claritatem insitam;</p>
      <p>Est usus legentis in iis qui facit eorum claritatem.</p>
      <p>Investigationes demonstraverunt lectores legere me lius quod ii legunt saepius. Claritas est etiam processus dynamicus, qui sequitur mutationem consuetudium lectorum. Mirum est notare quam littera gothica, quam nunc putamus parum claram, anteposuerit litterarum formas humanitatis per seacula quarta decima et quinta decima. Eodem modo typi, qui nunc nobis videntur parum clari, fiant sollemnes in futurum.</p>
      <p>consectetuer adipiscing elit, sed diam nonummy nibh euismod tincidunt ut laoreet dolore magna aliquam erat volutpat. Ut wisi enim ad minim veniam, quis nostrud exerci tation ullamcorper suscipit lobortis nisl ut aliquip ex ea commodo consequat. Duis autem vel eum iriure dolor in hendrerit in vulputate velit esse molestie consequat, vel illum dolore eu feugiat nulla facilisis at vero eros et accumsan et iusto odio dignissim qui blandit praesent luptatum zzril delenit augue duis dolore te feugait nulla facilisi.</p>
      <p>Nam liber tempor cum soluta nobis eleifend option congue nihil imperdiet .</p>
    </article>

    <div class="signature-mark" role="img" aria-label="Handwritten signature of Paul Renwick"></div>
    <section class="signatory">
      <div class="signatory-name">Paul Renwick</div>
      <div class="signatory-title">Managing Director</div>
    </section>
  </main>
</body>
</html>
```